Luxury Bath Flyer

I would like to have a professional Flyer, which would describe a beautiful atmospheric luxury-Bath situation. I am sending you a( screenshot) Flyer Proposal, which shoes my intention and wish how I would like to have it. Please note that Ästhetik and a professional Flyer is very important to me. If possible send a psd.file or a indesign file, in case of we gonna need to change the text. You are also free to make 2 different proposals and one as you would suggest.?(I send you couple pictures, but the main one which I choose on the pdf file, please keep that, it is called " KR-71" - If there is a question please let me know. Looking forward to receive an amazing artwork.Kind Regards Merle
Look and feel
Each slider illustrates characteristics of the customer's brand and the style your logo design should communicate.

```html
<!DOCTYPE html>
<html lang="en">
<head>
<meta charset="utf-8">
<title>Luxury Bath Flyer</title>
<link href="https://fonts.googleapis.com/css2?family=Archivo+Narrow:wght@600;700&display=swap" rel="stylesheet">
<style>
  :root {
    --paper: #ffffff;
    --blush: #f3d4d4;
    --amber: #f2a65c;
    --peach: #f9d3a7;
    --ink: #3b2414;
    --photo-light: #d9d6d1;
    --photo-mid: #a89b8c;
    --photo-dark: #6b5745;
  }
  * { margin: 0; padding: 0; box-sizing: border-box; }
  html, body { width: 849px; height: 1200px; overflow: hidden; background: var(--paper); }
  .flyer {
    position: relative; width: 849px; height: 1200px; background: var(--paper);
    font-family: "Archivo Narrow", "Arial Narrow", sans-serif; color: var(--ink);
    overflow: hidden;
  }
  .frame {
    position: absolute; left: 28px; top: 92px; width: 796px; height: 1062px;
    border: 42px solid var(--blush);
  }
  .site {
    position: absolute; left: 58px; top: 68px; font-size: 22px; font-weight: 700;
  }
  .brand {
    position: absolute; right: 30px; top: 62px; display: flex; align-items: center; gap: 10px;
    font-size: 28px; font-weight: 700; background: var(--paper); padding: 6px 10px;
  }
  .brand-mark { width: 22px; height: 22px; background: var(--amber); }
  .photo-frame { position: absolute; background: var(--amber); padding: 18px; }
  .photo-frame.hero { left: 33px; top: 130px; width: 614px; height: 316px; }
  .photo-frame.detail { left: 65px; top: 519px; width: 278px; height: 315px; }
  .photo { width: 100%; height: 100%; }
  .hero .photo { background: linear-gradient(100deg, var(--photo-dark) 0%, var(--photo-mid) 35%, var(--photo-light) 70%, #eeebe6 100%); }
  .detail .photo { background: linear-gradient(180deg, var(--photo-light) 0%, #c6bdb2 50%, var(--photo-mid) 100%); }
  .motto {
    position: absolute; left: 343px; top: 444px; width: 468px; height: 156px;
    background: var(--amber); padding: 22px 20px; font-size: 28px; font-weight: 700; line-height: 1.12;
  }
  .disc { position: absolute; border-radius: 50%; }
  .disc.services { left: 310px; top: 580px; width: 300px; height: 300px; background: var(--peach); }
  .disc.other { left: 470px; top: 760px; width: 340px; height: 340px; background: var(--peach); }
  .disc.contact { left: 22px; top: 920px; width: 250px; height: 250px; background: var(--amber); }
  .block { position: absolute; text-align: center; font-weight: 700; }
  .block h2 { font-size: 36px; font-weight: 700; line-height: 1.1; }
  .block p { font-size: 24px; line-height: 1.2; }
  .services-text { left: 370px; top: 650px; width: 180px; }
  .services-text h2 { text-align: left; margin-bottom: 8px; }
  .other-text { left: 500px; top: 870px; width: 280px; }
  .other-text h2 { text-align: left; padding-left: 22px; margin-bottom: 8px; }
  .contact-text { left: 40px; top: 1005px; width: 214px; }
  .contact-text p { font-size: 22px; line-height: 1.3; }
  .email { position: absolute; left: 332px; top: 1122px; font-size: 24px; font-weight: 700; }
</style>
</head>
<body>
<main class="flyer">
  <div class="frame"></div>
  <div class="site">www.YourSite.com</div>
  <div class="brand"><span class="brand-mark"></span>Wannhof</div>

  <div class="photo-frame hero"><div class="photo" role="img" aria-label="Photo of a luxury bathroom with freestanding tub, wooden vanity and tiled walls"></div></div>

  <div class="motto">Your Mottto should be here<br>Donec tempus a arcu nec ornare.<br>Vestibulum ante ipsum pgvfd fdr orci luctus</div>

  <div class="disc services"></div>
  <div class="disc other"></div>
  <div class="disc contact"></div>

  <div class="photo-frame detail"><div class="photo" role="img" aria-label="Photo of a bright bathroom interior with wood-look floor and vanity"></div></div>

  <section class="block services-text">
    <h2>Your services</h2>
    <p>Donec tempus<br>arcu nec ornare.<br>Vestibulum ante<br>ipsum primis in<br>luctus</p>
  </section>

  <section class="block other-text">
    <h2>Other Things</h2>
    <p>Donec tempus a arcu<br>Gc ornare.<br>Vestibulum ante ipsum<br>sin faucib luctus</p>
  </section>

  <section class="block contact-text">
    <p>Street Adress<br>143 Luctus 39 CC<br>Phone No.<br>0000292727</p>
  </section>

  <div class="email">YourEmail@co</div>
</main>
</body>
</html>
```